Whitmore Business Card Design

The name of the business is Dara Whitmore, CPA LLC
The service that we offer is Accounting, Tax & Consulting Services. I need it to have the following items:
Dara Whitmore, Principal
Phone Number
Email Address
Physical Address

I have attached the company logo, one in black and one in white. Please provide a design in black background and the other in white background. Please include "Accounting, Tax & Consulting Services". I want the business card to be clean and very professional.

```html
<!DOCTYPE html>
<html lang="en">
<head>
<meta charset="utf-8">
<title>Dara Whitmore, CPA LLC — Business Cards</title>
<link rel="stylesheet" href="https://fonts.googleapis.com/css2?family=Poppins:wght@400;500;600;700&display=swap">
<style>
  :root {
    --backdrop: #d4d4d4;
    --card-dark: #3b3b3d;
    --card-light: #ffffff;
    --ink: #333335;
    --muted: #8c8c8e;
    --brand-red: #9b1b1f;
    --band-grey: #3d3d40;
    --faint: #ececec;
    --rule: #c8c8c8;
  }
  * { box-sizing: border-box; margin: 0; padding: 0; }
  html, body { width: 1200px; height: 852px; overflow: hidden; }
  body {
    background: var(--backdrop);
    font-family: "Poppins", sans-serif;
    position: relative;
  }
  .card {
    position: absolute;
    width: 540px;
    height: 309px;
    box-shadow: 0 6px 18px rgba(0,0,0,.18);
    overflow: hidden;
  }

  /* Front */
  .card-front { left: 60px; top: 80px; background: var(--card-dark); }
  .front-lockup {
    position: absolute; left: 0; right: 0; top: 100px;
    display: flex; flex-direction: column; align-items: center; gap: 8px;
  }
  .lockup-row { display: flex; align-items: center; gap: 12px; }
  .lockup-mark { width: 26px; height: 26px; background: var(--brand-red); }
  .front-name { color: #fff; font-weight: 600; font-size: 25px; letter-spacing: .5px; }
  .front-tagline { color: var(--muted); font-weight: 600; font-size: 15px; letter-spacing: 1.6px; text-transform: uppercase; }
  .front-services { color: #bdbdbf; font-weight: 400; font-size: 11px; letter-spacing: .8px; }

  /* Back */
  .card-back { left: 600px; top: 470px; background: var(--card-light); }
  .back-decor {
    position: absolute; right: 40px; top: 18px;
    width: 112px; height: 112px; border: 14px solid var(--faint);
  }
  .back-lockup { position: absolute; left: 26px; top: 84px; display: flex; align-items: center; gap: 10px; }
  .back-lockup .lockup-mark { width: 30px; height: 30px; }
  .back-lockup-text { display: flex; flex-direction: column; }
  .back-name { color: var(--ink); font-weight: 600; font-size: 17px; line-height: 1.15; }
  .back-tagline { color: var(--muted); font-weight: 600; font-size: 10.5px; letter-spacing: 1.1px; text-transform: uppercase; }
  .back-services { color: var(--muted); font-size: 9.5px; letter-spacing: .3px; }

  .address {
    position: absolute; right: 26px; top: 146px;
    padding-top: 8px; border-top: 1px solid var(--rule);
    display: flex; gap: 6px; color: var(--ink); font-size: 11px; line-height: 1.45;
  }
  .address svg { flex: none; margin-top: 2px; }

  .person { position: absolute; left: 110px; top: 160px; }
  .person-name { color: var(--ink); font-weight: 600; font-size: 17px; letter-spacing: .4px; text-transform: uppercase; line-height: 1.2; }
  .person-role { color: var(--muted); font-weight: 600; font-size: 11px; letter-spacing: .8px; text-transform: uppercase; }
  .person-rule { width: 30px; height: 2px; background: var(--muted); margin: 5px 0 6px; }
  .contact { display: flex; align-items: center; gap: 7px; color: var(--ink); font-size: 11.5px; line-height: 1.6; }
  .bands { position: absolute; left: 0; bottom: 0; }
</style>
</head>
<body>
  <section class="card card-front" aria-label="Card front">
    <div class="front-lockup">
      <div class="lockup-row">
        <span class="lockup-mark"></span>
        <span class="front-name">Dara Whitmore, CPA LLC</span>
      </div>
      <span class="front-tagline">Certified Public Accountant</span>
      <span class="front-services">Accounting, Tax &amp; Consulting Services</span>
    </div>
  </section>

  <section class="card card-back" aria-label="Card back">
    <div class="back-decor"></div>
    <div class="back-lockup">
      <span class="lockup-mark"></span>
      <div class="back-lockup-text">
        <span class="back-name">Dara Whitmore, CPA LLC</span>
        <span class="back-tagline">Certified Public Accountant</span>
        <span class="back-services">Accounting, Tax &amp; Consulting Services</span>
      </div>
    </div>

    <div class="address">
      <svg width="10" height="13" viewBox="0 0 10 13" aria-hidden="true">
        <path d="M5 0a5 5 0 0 1 5 5c0 3.5-5 8-5 8S0 8.5 0 5a5 5 0 0 1 5-5z" fill="var(--brand-red)"/>
        <circle cx="5" cy="5" r="1.8" fill="#fff"/>
      </svg>
      <span>P.O. Box 218 5120 Elm Rd,<br>Bayview FL 30412</span>
    </div>

    <div class="person">
      <div class="person-name">Dara Whitmore</div>
      <div class="person-role">Principal</div>
      <div class="person-rule"></div>
      <div class="contact">
        <svg width="10" height="10" viewBox="0 0 10 10" aria-hidden="true">
          <path d="M2 0.5l1.8 2-1 1.2a6 6 0 0 0 3.5 3.5l1.2-1 2 1.8-1.2 1.5C4.5 9.5 0.5 5.5 0.5 1.7z" fill="var(--brand-red)"/>
        </svg>
        <span>555.014.2278</span>
      </div>
      <div class="contact">
        <svg width="11" height="8" viewBox="0 0 11 8" aria-hidden="true">
          <rect width="11" height="8" fill="var(--brand-red)"/>
          <path d="M0.5 0.8L5.5 4.6 10.5 0.8" stroke="#fff" stroke-width="1" fill="none"/>
        </svg>
        <span>DaraWhitmore@emailaddress.com</span>
      </div>
    </div>

    <svg class="bands" width="540" height="309" viewBox="0 0 540 309" aria-hidden="true">
      <polygon points="330,309 348,276 540,276 540,309" fill="var(--band-grey)"/>
      <polygon points="0,309 0,298 326,298 340,282 348,282 330,309" fill="var(--brand-red)"/>
    </svg>
  </section>
</body>
</html>
```